Artist needs a business card for her pencil portraits and streetscapes

My mum is an artist and does fabulous portraits and sketches with pencil and needs a business card.
She likes designs that are a bit weird or unusual. The winning design will NOT be a slick modern corporate looking logo. It should be a little bit rustic and different. Interesting patterns and textures would be great, it doesn't even need to look like a business card! Come up with something unique!

Target Market(s)

Older clientele looking for family portraits

Industry/Entity Type

Artists

Contact Information for Business Card

Basically just need the name and contact details

Font styles to use
Decorative
Script

Requirements
Must have
• Lena Brodsworth
• Artist
• 0427913562
• lenabrodsworth@quillpost.example
Nice to have
• Weird artistic backgrounds, interesting textures, unusual designs for an artistic woman.
Should not have
• Nothing ultra modern and nothing corporate looking.

```html
<!DOCTYPE html>
<html lang="en">
<head>
<meta charset="utf-8">
<title>Lena Brodsworth – Artist business card</title>
<link rel="stylesheet" href="https://fonts.googleapis.com/css2?family=Italianno&display=swap">
<style>
  :root {
    --backdrop: #e9ebec;
    --card: #ffffff;
    --petal: #7fd3d0;
    --petal-deep: #5fc3bf;
    --petal-pale: #e9f4f3;
    --name-teal: #1b8f8a;
    --ink-blue: #2a43a0;
    --card-shadow: 0 6px 18px rgba(0, 0, 0, 0.22);
  }

  * { box-sizing: border-box; margin: 0; padding: 0; }

  html, body {
    width: 1163px;
    height: 1200px;
    overflow: hidden;
    background: var(--backdrop);
  }

  .sheet {
    width: 1163px;
    height: 1200px;
    display: flex;
    flex-direction: column;
    align-items: center;
    justify-content: center;
    gap: 26px;
  }

  .card {
    position: relative;
    width: 980px;
    height: 560px;
    background: var(--card);
    box-shadow: var(--card-shadow);
    overflow: hidden;
  }

  .card__bloom {
    position: absolute;
    inset: 0;
    width: 100%;
    height: 100%;
  }

  .card__details {
    position: absolute;
    left: 696px;
    transform: translateX(-50%);
    text-align: center;
    font-family: "Italianno", cursive;
    white-space: nowrap;
  }

  .card__name {
    top: 128px;
    font-size: 78px;
    line-height: 1;
    font-weight: 400;
    color: var(--name-teal);
    letter-spacing: 1px;
  }

  .card__role {
    top: 196px;
    font-size: 42px;
    line-height: 1;
    color: var(--ink-blue);
  }

  .card__contact {
    top: 300px;
    font-size: 38px;
    line-height: 1.15;
    color: var(--ink-blue);
    font-style: normal;
  }
</style>
</head>
<body>
<main class="sheet">

  <section class="card card--front" aria-label="Business card front">
    <svg class="card__bloom" viewBox="0 0 420 240" preserveAspectRatio="none" aria-hidden="false">
      <defs>
        <radialGradient id="bloom-front" cx="30%" cy="55%" r="75%">
          <stop offset="0%" stop-color="var(--petal-deep)"/>
          <stop offset="55%" stop-color="var(--petal)"/>
          <stop offset="100%" stop-color="var(--petal-pale)"/>
        </radialGradient>
        <radialGradient id="bloom-corner" cx="100%" cy="100%" r="100%">
          <stop offset="0%" stop-color="var(--petal-deep)"/>
          <stop offset="60%" stop-color="var(--petal)"/>
          <stop offset="100%" stop-color="var(--petal-pale)"/>
        </radialGradient>
      </defs>
      <g role="img" aria-label="Illustration of turquoise chrysanthemum blooms with pale hydrangea petals along the left edge">
        <path d="M0 0 H150 C170 30 200 55 190 100 C205 140 200 190 178 240 H0 Z" fill="var(--petal-pale)"/>
        <path d="M0 0 H128 C142 30 168 60 160 100 C170 140 160 190 140 240 H0 Z" fill="url(#bloom-front)"/>
      </g>
      <g role="img" aria-label="Illustration of a turquoise bloom with pale petals in the lower right corner">
        <path d="M420 150 C380 160 350 190 340 240 H420 Z" fill="var(--petal-pale)"/>
        <path d="M420 178 C395 186 375 210 370 240 H420 Z" fill="url(#bloom-corner)"/>
      </g>
    </svg>

    <h1 class="card__details card__name">Lena Brodsworth</h1>
    <p class="card__details card__role">Artist</p>
    <address class="card__details card__contact">
      tel: 0427913562<br>
      mail: lenabrodsworth@quillpost.example
    </address>
  </section>

  <section class="card card--back" aria-label="Business card back">
    <svg class="card__bloom" viewBox="0 0 420 240" preserveAspectRatio="none">
      <defs>
        <radialGradient id="bloom-top" cx="10%" cy="10%" r="90%">
          <stop offset="0%" stop-color="var(--petal-deep)"/>
          <stop offset="55%" stop-color="var(--petal)"/>
          <stop offset="100%" stop-color="var(--petal-pale)"/>
        </radialGradient>
        <radialGradient id="bloom-sweep" cx="75%" cy="65%" r="70%">
          <stop offset="0%" stop-color="var(--petal-deep)"/>
          <stop offset="60%" stop-color="var(--petal)"/>
          <stop offset="100%" stop-color="var(--petal-pale)"/>
        </radialGradient>
      </defs>
      <g role="img" aria-label="Illustration of turquoise chrysanthemum blooms with pale petals in the top left corner">
        <path d="M0 0 H172 C160 40 120 80 70 110 C45 125 20 140 0 148 Z" fill="var(--petal-pale)"/>
        <path d="M0 0 H120 C112 35 80 70 40 88 C25 96 10 102 0 106 Z" fill="url(#bloom-top)"/>
      </g>
      <g role="img" aria-label="Illustration of large turquoise chrysanthemum blooms sweeping diagonally from the bottom centre to the top right">
        <path d="M145 240 C160 170 230 110 310 40 C340 15 380 5 420 0 V240 Z" fill="var(--petal-pale)"/>
        <path d="M178 240 C195 185 250 140 320 90 C355 65 390 45 420 38 V240 Z" fill="url(#bloom-sweep)"/>
      </g>
    </svg>
  </section>

</main>
</body>
</html>
```